Re-design of Business Card

We require a design for our business card.

Korrim is a supplier of industrial packaging specializing in plastic products. We are undergoing a rebranding to appear more corporate. We have changed our company name to korrim and have a new logo.

I have uploaded our old card design with the previous company name.
Don't copy the current design. We are looking for a new design.

Industry/Entity Type

Manufacturing

Contact Information for Business Card

please don't copy the current design. we are looking for a new design.

Font styles to use
Sans Serif

Colors

Designer to choose colors to be used in the design.

Requirements
Must have
• clean and easy to read.

```html
<!DOCTYPE html>
<html lang="en">
<head>
<meta charset="utf-8">
<title>Korrim Business Card</title>
<link href="https://fonts.googleapis.com/css2?family=PT+Sans:wght@400;700&family=Arimo:wght@400&display=swap" rel="stylesheet">
<style>
  :root {
    --orange: #f47c20;
    --ink: #1a1a1a;
    --white: #ffffff;
    --border: #222222;
    --page: #ffffff;
  }
  * { box-sizing: border-box; margin: 0; padding: 0; }
  html, body {
    width: 1062px; height: 1200px; overflow: hidden;
    background: var(--page);
  }
  body { position: relative; font-family: "PT Sans", sans-serif; color: var(--ink); }

  .card {
    position: absolute; left: 101px; width: 861px; height: 478px;
    border: 1.5px solid var(--border); background: var(--white); overflow: hidden;
  }
  .card--front { top: 94px; }
  .card--back { top: 627px; }

  /* Front */
  .wordmark {
    position: absolute; left: 39px; top: 35px; width: 781px; height: 253px;
    display: flex; align-items: center; justify-content: center;
    font-family: "PT Sans", sans-serif; font-weight: 700;
    font-size: 200px; letter-spacing: 6px; color: var(--orange); line-height: 1;
  }
  .services {
    position: absolute; left: 0; top: 301px; width: 100%; height: 160px;
  }
  .service {
    position: absolute; top: 0; height: 158px; padding-left: 15px;
  }
  .service--divided { border-left: 2px solid var(--orange); }
  .service:nth-child(1) { left: 38px; padding-left: 15px; }
  .service:nth-child(2) { left: 222px; }
  .service:nth-child(3) { left: 426px; }
  .service:nth-child(4) { left: 669px; }
  .service__title {
    font-weight: 700; font-size: 25px; line-height: 27px; margin-bottom: 3px;
  }
  .service__list { list-style: none; font-size: 18px; line-height: 23.5px; }
  .service__list li::before { content: "\2022"; margin-right: 2px; }
  .service__list .cont { padding-left: 10px; }
  .service__list .cont::before { content: none; }

  /* Back */
  .badge {
    position: absolute; left: 49px; width: 134px; height: 134px;
    border-radius: 50%; border: 10px solid var(--orange);
  }
  .badge:nth-of-type(1) { top: 23px; }
  .badge:nth-of-type(2) { top: 172px; }
  .badge:nth-of-type(3) { top: 322px; }
  .panel { position: absolute; inset: 0; width: 100%; height: 100%; }
  .contact { position: absolute; left: 444px; top: 52px; color: var(--white); }
  .contact__name { font-weight: 700; font-size: 31px; line-height: 34px; }
  .contact__role { font-size: 18px; line-height: 22px; margin-bottom: 14px; }
  .contact__list { list-style: none; font-family: "Arimo", sans-serif; font-size: 25px; }
  .contact__row { display: flex; align-items: flex-start; height: 40.5px; }
  .contact__icon { width: 34px; height: 30px; flex: none; }
  .contact__sep { width: 29px; text-align: center; flex: none; }
  .contact__row--address { height: auto; line-height: 34px; }
  .contact__row--address .contact__icon { margin-top: 2px; }
</style>
</head>
<body>

<section class="card card--front" aria-label="Card front">
  <div class="wordmark">KORRIM</div>
  <div class="services">
    <div class="service">
      <h2 class="service__title">Pallet<br>Containment</h2>
      <ul class="service__list"><li>Stretch</li><li>Heat Shrunk</li><li>Pallet Hood</li></ul>
    </div>
    <div class="service service--divided">
      <h2 class="service__title">Flexible<br>Packaging</h2>
      <ul class="service__list"><li>Bags &amp; Liners &bull;Tube</li><li>Film &amp; Sheet</li><li>Printed films (12 col)</li><li>Shrink films</li></ul>
    </div>
    <div class="service service--divided">
      <h2 class="service__title">Pallet Wrapping<br>Machinery</h2>
      <ul class="service__list"><li>Semi &amp; Fully Auto Lines</li><li>Finance options include</li><li class="cont">Lease, Rent, pay per wrap</li></ul>
    </div>
    <div class="service service--divided">
      <h2 class="service__title">General<br>Packaging</h2>
    </div>
  </div>
</section>

<section class="card card--back" aria-label="Card back">
  <svg class="panel" viewBox="0 0 861 478" aria-hidden="true">
    <polygon points="393,0 861,0 861,478 452,478 264,196" fill="var(--orange)"/>
  </svg>
  <div class="badge" role="img" aria-label="Distribution badge"></div>
  <div class="badge" role="img" aria-label="Food safety certification badge"></div>
  <div class="badge" role="img" aria-label="Quality certification badge"></div>

  <div class="contact">
    <h1 class="contact__name">Dana Whitfield</h1>
    <p class="contact__role">Machinery Sales Manager</p>
    <ul class="contact__list">
      <li class="contact__row">
        <svg class="contact__icon" viewBox="0 0 34 30" aria-label="Mobile"><rect x="11" y="1" width="12" height="27" rx="2" fill="none" stroke="#fff" stroke-width="2"/><rect x="13" y="5" width="8" height="16" fill="#fff"/><circle cx="17" cy="24.5" r="1.3" fill="#fff"/></svg>
        <span class="contact__sep">:</span><span>XXX-XXX-XXXX</span>
      </li>
      <li class="contact__row">
        <svg class="contact__icon" viewBox="0 0 34 30" aria-label="Email"><rect x="3" y="8" width="28" height="20" fill="#fff"/><path d="M3 8 L17 19 L31 8" fill="none" stroke="var(--orange)" stroke-width="1.5"/></svg>
        <span class="contact__sep">:</span><span>dana@korrim.au</span>
      </li>
      <li class="contact__row">
        <svg class="contact__icon" viewBox="0 0 34 30" aria-label="Phone"><path d="M3 10 Q17 0 31 10 L28 14 L23 12 L23 9 Q17 7 11 9 L11 12 L6 14 Z" fill="#fff"/><path d="M9 14 L25 14 L29 27 L5 27 Z" fill="#fff"/></svg>
        <span class="contact__sep">:</span><span>130 048 1736</span>
      </li>
      <li class="contact__row">
        <svg class="contact__icon" viewBox="0 0 34 30" aria-label="Fax"><rect x="10" y="1" width="14" height="10" fill="#fff"/><rect x="3" y="12" width="28" height="16" rx="2" fill="#fff"/><rect x="9" y="16" width="16" height="3" fill="var(--orange)"/></svg>
        <span class="contact__sep">:</span><span>+617 3480 5127</span>
      </li>
      <li class="contact__row">
        <svg class="contact__icon" viewBox="0 0 34 30" aria-label="Website"><circle cx="17" cy="15" r="13" fill="#fff"/><g fill="none" stroke="var(--orange)" stroke-width="1.3"><ellipse cx="17" cy="15" rx="6" ry="13"/><line x1="4" y1="15" x2="30" y2="15"/><line x1="17" y1="2" x2="17" y2="28"/></g></svg>
        <span class="contact__sep">:</span><span>www.lendarpackaging.com.au</span>
      </li>
      <li class="contact__row contact__row--address">
        <svg class="contact__icon" viewBox="0 0 34 30" aria-label="Address"><path d="M17 29 L8 14 A10 10 0 1 1 26 14 Z" fill="#fff"/><circle cx="17" cy="10" r="3.5" fill="var(--orange)"/></svg>
        <span class="contact__sep">:</span><span>117 Fenwick Rd,<br>Carrowbank, Qld 4112<br>Australia</span>
      </li>
    </ul>
  </div>
</section>

</body>
</html>
```